Robotic startup business cards

We are looking for a design for a set of business cards which reflect the spirit and humor of Torvexa Robotics. We want to present ourselves as sleek, professional, but laid-back consulting company.

We primarily focus on developing robotic arms software. This software controls robots and does things like grab items, pick objects up, move them, etc.

We want to allow you maximum design creativity, but do ask that you consider our existing style guidelines (see attached files) in order to make our brand cohesive.

Target Market(s)

Startups and Mid-size robotic companies

Industry/Entity Type

Business

Contact Information for Business Card

Liam Brantly, PhD
Roboticist | Torvexa Consulting | 318.572.6094

Font styles to use
Other font styles liked:
• Source code pro

Requirements
Must have
• robots or robotic arms
• similar color scheme that works with existing brand guidelines
Nice to have
• please consider our existing style guidelines (see attached files) in order to make our brand cohesive.
• minimalism style is generally nice.
Should not have
• An old, boring, or corporate feel. Too much text.

```html
<!DOCTYPE html>
<html lang="en">
<head>
<meta charset="utf-8">
<title>Torvexa Robotics – Business Cards</title>
<link href="https://fonts.googleapis.com/css2?family=Source+Code+Pro:wght@300;400;600;700&display=swap" rel="stylesheet">
<style>
  :root {
    --backdrop: #e9e4dc;
    --card-black: #050505;
    --brand-green: #5cc196;
    --paper-white: #f4f4f4;
    --shadow: rgba(0, 0, 0, 0.28);
  }
  * { margin: 0; padding: 0; box-sizing: border-box; }
  html, body {
    width: 1200px;
    height: 800px;
    overflow: hidden;
  }
  body {
    background: var(--backdrop);
    font-family: "Source Code Pro", monospace;
    position: relative;
  }
  .card {
    position: absolute;
    width: 520px;
    height: 297px;
    background: var(--card-black);
    box-shadow: 0 14px 30px var(--shadow);
  }
  .card--front { left: 70px; top: 170px; }
  .card--back { left: 610px; top: 330px; }

  /* Front: name mark */
  .brand-mark {
    position: absolute;
    inset: 0;
    display: flex;
    align-items: center;
    justify-content: center;
    gap: 22px;
  }
  .brand-mark__dot {
    width: 36px;
    height: 36px;
    border-radius: 50%;
    background: var(--brand-green);
  }
  .brand-mark__name {
    font-size: 38px;
    font-weight: 300;
    letter-spacing: 9px;
    color: var(--paper-white);
  }

  /* Back: contact side */
  .identity {
    position: absolute;
    left: 34px;
    top: 30px;
    padding-left: 20px;
  }
  .identity__bar {
    position: absolute;
    left: 0;
    top: 2px;
    width: 7px;
    height: 44px;
    background: var(--brand-green);
  }
  .identity__name {
    font-size: 19px;
    font-weight: 400;
    color: var(--paper-white);
    line-height: 1.1;
    letter-spacing: 0.5px;
  }
  .identity__name strong { font-weight: 700; }
  .identity__name small { font-size: 15px; font-weight: 400; }
  .identity__role {
    font-size: 19px;
    color: var(--brand-green);
    line-height: 1.15;
  }
  .contact {
    position: absolute;
    left: 34px;
    bottom: 40px;
    font-size: 15px;
    line-height: 1.3;
  }
  .contact__company {
    color: var(--paper-white);
    font-weight: 600;
    font-size: 16px;
    margin-bottom: 2px;
  }
  .contact__line { color: var(--brand-green); }
  .accent-shape {
    position: absolute;
    right: 46px;
    top: 58px;
  }
</style>
</head>
<body>
  <section class="card card--front" aria-label="Business card front">
    <div class="brand-mark">
      <span class="brand-mark__dot"></span>
      <span class="brand-mark__name">TORVEXA</span>
    </div>
  </section>

  <section class="card card--back" aria-label="Business card back">
    <div class="identity">
      <span class="identity__bar"></span>
      <p class="identity__name">LIAM<strong>BRANTLY</strong>,<small>PhD</small></p>
      <p class="identity__role">Roboticist</p>
    </div>
    <div class="contact">
      <p class="contact__company">TORVEXA Consulting</p>
      <p class="contact__line">318.572.6094</p>
      <p class="contact__line">email@TorvexaConsulting.com</p>
    </div>
    <svg class="accent-shape" width="180" height="180" viewBox="0 0 180 180" aria-hidden="true">
      <circle cx="90" cy="90" r="90" fill="var(--brand-green)"/>
    </svg>
  </section>
</body>
</html>
```